Aged Care Consultancy Business needs a business card design

I need a two sided business card - I want it clean and professional. Surprise me

Target Market(s)

middle aged and ageing victorians

Industry/Entity Type

Health Care

Contact Information for Business Card

Text to be included

Logo
Aged Care Consulting Services
Professional, Reliable, Affordable

Tovan Brelsick
Director
0427 31 64 92 (larger)
1300 73 29 41
tovan@wadolire.com.au
www.wadolcare.com.au
Facebook (details TBA)

include little icons beside the contact info:

- Envelope = email
- Phone = phone
- Globe = website

Font styles to use
Serif
Sans Serif

Requirements
Must have
• look proffesional and clean

```html
<!DOCTYPE html>
<html lang="en">
<head>
<meta charset="utf-8">
<title>wadol care — business card</title>
<link rel="stylesheet" href="https://fonts.googleapis.com/css2?family=Libre+Franklin:wght@400;600;700&display=swap">
<style>
  :root {
    --backdrop: #2f3033;
    --card-white: #ffffff;
    --brand-blue: #1f4f8f;
    --brand-blue-dark: #163c72;
    --brand-orange: #e8961a;
    --brand-orange-deep: #d98510;
    --ink-grey: #4a4a4a;
  }
  * { box-sizing: border-box; margin: 0; padding: 0; }
  html, body { width: 1200px; height: 843px; overflow: hidden; }
  body {
    background: var(--backdrop);
    font-family: "Libre Franklin", Arial, sans-serif;
    display: flex;
    align-items: center;
    justify-content: center;
    gap: 40px;
  }
  .card {
    position: relative;
    width: 540px;
    height: 309px;
    overflow: hidden;
  }

  /* Back side */
  .card-back {
    background: linear-gradient(160deg, var(--brand-orange) 0%, var(--brand-orange-deep) 100%);
    color: var(--card-white);
  }
  .card-back .brand-lockup {
    position: absolute;
    left: 0; right: 0; top: 112px;
    display: flex;
    justify-content: center;
    align-items: center;
    gap: 12px;
  }
  .card-back .brand-dot { width: 18px; height: 18px; border-radius: 50%; background: var(--card-white); }
  .card-back .brand-name { font-size: 44px; font-weight: 600; letter-spacing: 0.5px; color: var(--card-white); }
  .card-back .tagline {
    position: absolute;
    left: 30px; right: 30px; bottom: 26px;
    display: flex;
    justify-content: space-between;
    font-size: 12px;
    letter-spacing: 0.3px;
  }

  /* Front side */
  .card-front { background: var(--card-white); }
  .card-front .brand-lockup {
    position: absolute;
    left: 36px; top: 44px;
    display: flex;
    align-items: center;
    gap: 10px;
  }
  .card-front .brand-dot { width: 18px; height: 18px; border-radius: 50%; background: var(--brand-orange); }
  .card-front .brand-name { font-size: 40px; font-weight: 600; color: var(--brand-blue); letter-spacing: 0.5px; }
  .person { position: absolute; left: 38px; top: 118px; }
  .person-name { font-size: 19px; font-weight: 700; color: var(--brand-blue-dark); }
  .person-role { font-size: 14px; color: var(--brand-orange); margin-top: 2px; }

  .contact-list {
    position: absolute;
    right: 28px; bottom: 30px;
    list-style: none;
    text-align: right;
    color: var(--ink-grey);
  }
  .contact-list li {
    display: flex;
    justify-content: flex-end;
    align-items: center;
    gap: 8px;
    font-size: 13px;
    line-height: 20px;
  }
  .contact-list li.primary-phone { font-size: 24px; line-height: 32px; letter-spacing: 1px; }
  .contact-icon { width: 14px; height: 14px; flex: none; }
  .social-mark { width: 13px; height: 13px; background: var(--brand-blue); border-radius: 2px; flex: none; margin-right: 1px; }

  .base-band { position: absolute; left: 0; right: 0; bottom: 0; height: 10px; display: flex; }
  .base-band .band-blue { width: 46%; background: var(--brand-blue); }
  .base-band .band-orange { flex: 1; background: var(--brand-orange); }
</style>
</head>
<body>

  <section class="card card-back" aria-label="Card back">
    <div class="brand-lockup">
      <span class="brand-dot"></span>
      <span class="brand-name">wadol care</span>
    </div>
    <div class="tagline">
      <span>Aged Care Consulting Services</span>
      <span>Professional, Reliable, Affordable</span>
    </div>
  </section>

  <section class="card card-front" aria-label="Card front">
    <div class="brand-lockup">
      <span class="brand-dot"></span>
      <span class="brand-name">wadol care</span>
    </div>

    <div class="person">
      <div class="person-name">Tovan Brelsick</div>
      <div class="person-role">Director</div>
    </div>

    <ul class="contact-list">
      <li class="primary-phone">0427 31 64 92
        <svg class="contact-icon" viewBox="0 0 16 16" aria-hidden="true"><path fill="#1f4f8f" d="M3.5 1.5l2.5 0 1 3.5-1.6 1.2a8 8 0 0 0 4.4 4.4L11 9l3.5 1v2.5c0 1-1 2-2 2C6.5 14.5 1.5 9.5 1.5 3.5c0-1 1-2 2-2z"/></svg>
      </li>
      <li>1300 73 29 41
        <svg class="contact-icon" viewBox="0 0 16 16" aria-hidden="true"><path fill="#1f4f8f" d="M3.5 1.5l2.5 0 1 3.5-1.6 1.2a8 8 0 0 0 4.4 4.4L11 9l3.5 1v2.5c0 1-1 2-2 2C6.5 14.5 1.5 9.5 1.5 3.5c0-1 1-2 2-2z"/></svg>
      </li>
      <li>tovan@wadolire.com.au
        <svg class="contact-icon" viewBox="0 0 16 16" aria-hidden="true"><rect x="1" y="3" width="14" height="10" rx="1" fill="#1f4f8f"/><path d="M1.5 3.8L8 9l6.5-5.2" fill="none" stroke="#fff" stroke-width="1.2"/></svg>
      </li>
      <li>www.wadolcare.com.au
        <svg class="contact-icon" viewBox="0 0 16 16" aria-hidden="true"><g fill="none" stroke="#1f4f8f" stroke-width="1.3"><circle cx="8" cy="8" r="6.5"/><ellipse cx="8" cy="8" rx="2.8" ry="6.5"/><path d="M1.5 8h13M2.5 4.8h11M2.5 11.2h11"/></g></svg>
      </li>
      <li>wadolcare
        <span class="social-mark" aria-hidden="true"></span>
      </li>
    </ul>

    <div class="base-band" aria-hidden="true">
      <span class="band-blue"></span>
      <span class="band-orange"></span>
    </div>
  </section>

</body>
</html>
```